Book cover design for Safety Training Guide

We need a new cover for our book called “Worksite Crate Chats”

We need you to design 2 pieces:
The front cover--- Width: 10 inches Height: 11 inches
The book spine--- Width: 1.5 inches Height: 11 inches
We do NOT need a back cover.

The cover should be a clean, modern design. It must include the book title and our company logo (attached).

OPTIONAL: You can also include-- "52 Ready-to-Go Safety Meetings" but it is not required.

These are our company colors. It is not required to use these colors, but you may if you would like.
Main- Blue: 007da6
Acent 1- Yellow: ffd00d
Acent 2-Grey: 989999
Acent 3-Green: 91be4a

-------------------------------------------------------------------------
This is a description of the book. It should NOT be included in the design, I am only including it here to make you familiar with what the book is about
-------------------------------------------------------------------

Introducing Worksite Crate Chats: 52 Meeting Topics to Train Employees on Critical Safety Issues & WKPA Regulations. This 200+ page resource gives you everything you need for a full year's worth of high-impact weekly safety meetings.

For each meeting topic you'll receive:
1) A Meeting Leader Discussion Guide
2) An Employee Quiz
3) An Employee Handout
4) And a Case Study sheet that gives you true stories to illustrate key points

Effective Safety Meetings Made Easy

Preparing for regular safety meetings is a time consuming process. Sure, you can wing it and cover some basic points off the top of your head, but truly effective meetings require preparation.

To lead meetings that workers take seriously you have to: 1) be absolutely certain that you cover all of the key points, 2) come up with follow up questions to generate worthwhile discussion, 3) put together a quiz so you can document that workers learned the material and 4) develop a handout to reinforce your training.

That's why we put together Worksite Crate Chats: 52 Meeting Topics to Train Employees on Critical Safety Issues & WKPA Regulations.

Each meeting is made up of four color-coded pages.

BLUE Pages = Meeting Leader Discussion Guides. These sheets are for you. Use them to direct your team through the lesson and encourage participation.

WHITE Pages = Employee Quizes. Copy and distribute these to all meeting participants to ensure that they understand the content. Have them date and sign completed quizzes so you can document that they have received training.

BEIGE Pages = Employee Handouts. Copy and distribute these to all meeting participants so they have something to review after the meeting. They're a great way to reinforce the message.

PINK Pages = Case Studies. These sheets are also for you. Read these real-life scenarios to meeting participants to drive home the point that ignoring safety has serious consequences.

Bottom line: If the Worksite Crate Chats guide helps you hold even one additional meeting over the course of the year that prevents a workplace injury, your investment will be returned many times over.

Topics covered:
Bloodborne Pathogens
Crane Safety
Confined Space Safety
Emergency Evacuation
Operating forklifts safely
Forklift safety
Compressed air safety
Machine guarding safety
Using pallet jacks the safe way
Working safely around conveyors
Avoiding back strains
Avoiding musculoskeletal disorders
Safe lifting
Fall Protection
Fire Prevention
Hazard Communication
Housekeeping for safety
Avoid slip and trip hazards
Injury Prevention
Lockout / Tagout
---------------------------------------------------------------------------------------------

Please please comment if you have any questions. We will very quickly respond to your questions.

Thanks,
Marta
Harbor Nine Publishing

```html
<!DOCTYPE html>
<html lang="en">
<head>
<meta charset="utf-8">
<title>Worksite Crate Chats – Cover</title>
<link rel="stylesheet" href="https://fonts.googleapis.com/css2?family=Anton&family=Arimo:wght@700&display=swap">
<style>
  :root {
    --brand-blue: #1686ad;
    --deep-blue: #0a4f9e;
    --bright-blue: #2aa6f0;
    --night-blue: #061a4a;
    --brand-yellow: #fecb0a;
    --brand-grey: #9a9a9a;
    --white: #ffffff;
  }
  * { margin: 0; padding: 0; box-sizing: border-box; }
  html, body {
    width: 1200px;
    height: 1147px;
    overflow: hidden;
    background: var(--white);
  }
  .cover {
    position: relative;
    width: 1200px;
    height: 1147px;
    background: var(--brand-yellow);
    overflow: hidden;
    font-family: "Arimo", Arial, sans-serif;
  }
  .spine {
    position: absolute;
    left: 0;
    top: 0;
    width: 157px;
    height: 1147px;
    background: var(--brand-yellow);
  }
  .spine-brand {
    position: absolute;
    left: 13px;
    top: 13px;
    width: 131px;
    height: 174px;
    background: var(--brand-blue);
    display: flex;
    align-items: center;
    justify-content: center;
    text-align: center;
    color: var(--brand-yellow);
    font-weight: 700;
    font-size: 26px;
    line-height: 1.1;
  }
  .spine-title {
    position: absolute;
    left: 80px;
    top: 643px;
    transform: translate(-50%, -50%) rotate(90deg);
    white-space: nowrap;
    color: var(--brand-blue);
    font-weight: 700;
    font-size: 50px;
    letter-spacing: 0.5px;
  }
  .front {
    position: absolute;
    left: 157px;
    top: 0;
    width: 1019px;
    height: 1147px;
    background: var(--brand-blue);
  }
  .title {
    position: absolute;
    left: 0;
    width: 1019px;
    top: 30px;
    text-align: center;
    font-family: "Anton", Impact, sans-serif;
    font-size: 112px;
    line-height: 1.1;
    letter-spacing: 1px;
    color: var(--brand-grey);
    -webkit-text-stroke: 3px var(--brand-yellow);
    paint-order: stroke fill;
  }
  .count {
    position: absolute;
    left: 0;
    width: 1019px;
    top: 200px;
    text-align: center;
    color: var(--brand-yellow);
    font-weight: 700;
    font-size: 104px;
    line-height: 1;
  }
  .subtitle {
    position: absolute;
    left: 0;
    width: 1019px;
    top: 328px;
    text-align: center;
    color: var(--brand-yellow);
    font-weight: 700;
    font-size: 52px;
    line-height: 1.1;
  }
  .hero {
    position: absolute;
    left: 283px;
    top: 433px;
    width: 736px;
    height: 614px;
    background:
      radial-gradient(ellipse at 55% 35%, var(--bright-blue) 0%, transparent 55%),
      linear-gradient(180deg, var(--deep-blue) 0%, #1a6fd6 60%, var(--night-blue) 100%);
  }
  .brand-badge {
    position: absolute;
    left: 29px;
    top: 627px;
    width: 212px;
    height: 212px;
    border-radius: 50%;
    background: var(--brand-yellow);
    display: flex;
    align-items: center;
    justify-content: center;
    text-align: center;
    color: var(--white);
    font-weight: 700;
    font-size: 36px;
    line-height: 1.1;
  }
</style>
</head>
<body>
  <main class="cover">
    <aside class="spine">
      <div class="spine-brand">Harbor<br>Nine</div>
      <div class="spine-title">Ready-to-Go Safety Meetings</div>
    </aside>
    <section class="front">
      <h1 class="title">WORKSITE CRATE CHATS</h1>
      <div class="count">52</div>
      <div class="subtitle">Ready-to-Go Safety Meetings</div>
      <div class="hero" role="img" aria-label="Glowing blue digital security graphic with fingerprint and network icons above silhouettes of a team meeting around a table"></div>
      <div class="brand-badge">Harbor<br>Nine</div>
    </section>
  </main>
</body>
</html>
```